verdant terraces simple classy business card design

my name is owen harlow and I run a gardening business aimed at high class verdant terraces. the business name is verdant terraces and our logo was designed on pixel forum .My clientel are anything from residential homes to businesses. I take pride in my work and know that I offer a service like no other in my area.
The business card will be used to represent my business and I want it to be not only rememberable, but simplistic and modern. Eye catching too. Of course I would like it relatable to gardening and appealing to the correct clientel - those being garden enthusiasts, prestigious homes and businesses that are after top of the line gardening services like no other on the market.
I am not a typical lawn mowing business so I don't want a typical card design that represents that. The gardens I work with are generally million dollar properties with owners who are very garden proud looking for upkeep and guidance from me along with sometimes whole new garden designs. I want the business cards to show to my clients that I take pride, as they do, in their garden. And I want them to know from my card that I am a professional, qualified horticulturist offering them a top of the line service for life. I want them to refer my business on. I want them to look at my business card and see class and professionalism in a modern unique bold way.
The card should be simple with the possibility of the logo on the front being embossed/debossed and my details on the back the card should have a organic garden feel it's very important to me that it is absolutely perfect
I am also very open to ideas and suggestions so look forward to seeing the designs. the business logo has been supplied with this project and I want the card to be double sided

Contact info is
Owen Harlow - Managing Director / Horticulturist
Phone : 0481 526 704
Email: owenharlow@verdantterraces.com.au

Target Market(s)

high class gardens residential and commercial

Industry/Entity Type

Gardener

Contact Information for Business Card

Contact info is
Phone : 0481 526 704

PLEASE MAKE CARD DOUBLE SIDED

Requirements
Must have
• organic simple classy modern feel
• must flow with the current logo that has been supplied with this project
• Double sided
• Must explain in a simple way that I deal with high end gardens and I'm a qualified horticulturist
Nice to have
• embossed debossed logo
Should not have
• shouldn't be to busy or cheap looking

```html
<!DOCTYPE html>
<html lang="en">
<head>
<meta charset="utf-8">
<title>Verdant Terraces — Business Card</title>
<link rel="stylesheet" href="https://fonts.googleapis.com/css2?family=Questrial&display=swap">
<style>
  :root {
    --canvas-bg: #e9e4dc;
    --card-bg: #2f2b2c;
    --leaf-green: #5caf5f;
    --leaf-green-soft: #4f9a53;
    --card-shadow: rgba(40, 28, 18, 0.35);
  }
  * { box-sizing: border-box; margin: 0; padding: 0; }
  html, body {
    width: 1200px;
    height: 1050px;
    overflow: hidden;
    background: var(--canvas-bg);
    font-family: "Questrial", "Century Gothic", sans-serif;
  }
  .canvas {
    position: relative;
    width: 1200px;
    height: 1050px;
  }
  .card {
    position: absolute;
    left: 220px;
    width: 760px;
    height: 434px;
    background: var(--card-bg);
    box-shadow: 0 14px 30px var(--card-shadow);
    color: var(--leaf-green);
    overflow: hidden;
  }
  .card--front { top: 70px; }
  .card--back { top: 546px; }

  /* Front: brand name */
  .brand {
    position: absolute;
    inset: 0;
    display: flex;
    align-items: center;
    justify-content: center;
    gap: 22px;
  }
  .brand__dot {
    width: 54px;
    height: 54px;
    border-radius: 50%;
    background: var(--leaf-green);
  }
  .brand__name {
    font-size: 50px;
    letter-spacing: 6px;
    text-transform: uppercase;
    color: var(--leaf-green);
  }

  /* Back: contact details */
  .details {
    position: absolute;
    left: 70px;
    top: 168px;
    width: 350px;
  }
  .details__name {
    font-size: 27px;
    font-weight: 400;
    letter-spacing: 0.5px;
  }
  .details__role {
    margin-top: 10px;
    font-size: 17px;
    color: var(--leaf-green-soft);
  }
  .details__rule {
    margin: 28px 0 24px;
    width: 320px;
    height: 2px;
    background: var(--leaf-green-soft);
    border: 0;
  }
  .contact {
    list-style: none;
  }
  .contact__item {
    display: flex;
    align-items: center;
    gap: 16px;
    font-size: 18px;
    margin-bottom: 16px;
    white-space: nowrap;
  }
  .contact__icon {
    width: 20px;
    height: 20px;
    flex: none;
  }
  .emblem {
    position: absolute;
    left: 470px;
    top: 40px;
    width: 260px;
    height: 360px;
    background: radial-gradient(ellipse 50% 50% at 50% 50%, rgba(92,175,95,0.45), rgba(92,175,95,0.1) 80%, transparent 100%);
  }
</style>
</head>
<body>
<main class="canvas">
  <section class="card card--front" aria-label="Business card front">
    <div class="brand">
      <span class="brand__dot" aria-hidden="true"></span>
      <span class="brand__name">Verdant Terraces</span>
    </div>
  </section>

  <section class="card card--back" aria-label="Business card back">
    <div class="details">
      <h1 class="details__name">Owen Harlow</h1>
      <p class="details__role">Managing Director / Horticulturist</p>
      <hr class="details__rule">
      <ul class="contact">
        <li class="contact__item">
          <svg class="contact__icon" viewBox="0 0 24 24" aria-hidden="true">
            <path fill="var(--leaf-green)" d="M6.6 10.8a15.1 15.1 0 0 0 6.6 6.6l2.2-2.2a1 1 0 0 1 1-.25 11.4 11.4 0 0 0 3.6.57 1 1 0 0 1 1 1V20a1 1 0 0 1-1 1A17 17 0 0 1 3 4a1 1 0 0 1 1-1h3.5a1 1 0 0 1 1 1c0 1.250.2 2.450.57 3.57a1 1 0 0 1-.25 1z"/>
          </svg>
          <span>0481 526 704</span>
        </li>
        <li class="contact__item">
          <svg class="contact__icon" viewBox="0 0 24 24" aria-hidden="true">
            <path fill="none" stroke="var(--leaf-green)" stroke-width="1.8" d="M3 10l9-6 9 6v10H3z M3 10l9 6 9-6"/>
          </svg>
          <span>owenharlow@verdantterraces.com.au</span>
        </li>
      </ul>
    </div>
    <div class="emblem" role="img" aria-label="Large green brand emblem decoration"></div>
  </section>
</main>
</body>
</html>
```